Business Card Design

We are looking for a double sided business card.

On one side would be our logo

On the Other Side

Daniel Workby
Sales and Marketing

Phone/Text Logo and 530-471-6328
Email Logo and info@gildedcritters.example
Website Logo and www.gildedcritters.example
Facebook Logo and gilded critters
Instagram Logo and gilded_critters

Target Market(s)

Pet owners

Contact Information for Business Card

In project description

Requirements
Must have
• Logo

```html
<!DOCTYPE html>
<html lang="en">
<head>
<meta charset="utf-8">
<title>Gilded Critters – Business Card</title>
<link rel="stylesheet" href="https://fonts.googleapis.com/css2?family=Roboto:wght@400;500;700;900&display=swap">
<style>
  :root {
    --stage: #161617;
    --card-face: #262627;
    --card-face-deep: #1f1f20;
    --edge-yellow: #ffd21a;
    --edge-orange: #ff8c00;
    --accent: #ff9a0a;
    --accent-bright: #ffb400;
    --text-light: #f2f2f2;
    --rule: #d9d9d9;
  }
  * { box-sizing: border-box; margin: 0; padding: 0; }
  html, body { width: 1200px; height: 840px; overflow: hidden; }
  body {
    background: var(--stage);
    font-family: "Roboto", Arial, sans-serif;
    color: var(--text-light);
    display: flex;
    align-items: center;
    justify-content: center;
    gap: 30px;
  }
  .card {
    width: 560px;
    height: 324px;
    border-radius: 28px;
    padding: 0 0 4px 3px;
    background: linear-gradient(160deg, var(--edge-yellow), var(--edge-orange));
  }
  .card-face {
    position: relative;
    width: 100%;
    height: 100%;
    border-radius: 26px;
    background: linear-gradient(150deg, var(--card-face), var(--card-face-deep));
    overflow: hidden;
  }

  /* Front: brand side */
  .brand-front {
    position: absolute;
    left: 0; right: 0; top: 0; bottom: 0;
    display: flex;
    flex-direction: column;
    align-items: center;
    justify-content: center;
    gap: 14px;
  }
  .brand-lockup { display: flex; align-items: center; gap: 14px; }
  .brand-dot {
    width: 22px; height: 22px; border-radius: 50%;
    background: var(--accent);
  }
  .brand-name {
    font-weight: 900;
    font-size: 46px;
    letter-spacing: 1px;
    color: var(--text-light);
    text-transform: uppercase;
  }
  .brand-url {
    font-size: 13px;
    font-weight: 500;
    letter-spacing: 4px;
    color: var(--accent);
    text-transform: uppercase;
  }

  /* Back: contact side */
  .brand-back {
    position: absolute;
    right: 34px; top: 40px;
    display: flex; align-items: center; gap: 10px;
  }
  .brand-back .brand-dot { width: 16px; height: 16px; }
  .brand-back .brand-name { font-size: 30px; }
  .brand-rule {
    position: absolute;
    right: 34px; top: 92px;
    width: 300px; height: 1px;
    background: var(--rule);
  }
  .person {
    position: absolute;
    left: 40px; top: 150px;
    width: 240px;
  }
  .person-name {
    font-weight: 900;
    font-size: 24px;
    color: var(--accent);
    text-transform: uppercase;
    line-height: 1.1;
  }
  .person-title {
    font-size: 17px;
    color: var(--text-light);
    margin-top: 2px;
  }
  .person-rule {
    margin-top: 10px;
    height: 1px;
    background: var(--rule);
  }
  .contact-list {
    position: absolute;
    left: 40px; top: 224px;
    list-style: none;
  }
  .contact-list li,
  .social-list li {
    display: flex; align-items: center; gap: 9px;
    font-size: 15px;
    line-height: 24px;
  }
  .contact-icon { width: 14px; height: 14px; flex: none; }
  .social-list {
    position: absolute;
    right: 34px; top: 112px;
    list-style: none;
  }
  .social-mark {
    width: 12px; height: 12px; border-radius: 3px;
    background: var(--accent);
    flex: none;
  }
</style>
</head>
<body>

  <section class="card card-front" aria-label="Business card front">
    <div class="card-face">
      <div class="brand-front">
        <div class="brand-lockup">
          <span class="brand-dot"></span>
          <span class="brand-name">Gilded Critters</span>
        </div>
        <p class="brand-url">www.gildedcritters.example</p>
      </div>
    </div>
  </section>

  <section class="card card-back" aria-label="Business card back">
    <div class="card-face">
      <div class="brand-back">
        <span class="brand-dot"></span>
        <span class="brand-name">Gilded Critters</span>
      </div>
      <div class="brand-rule"></div>

      <ul class="social-list">
        <li><span class="social-mark"></span>gilded critters</li>
        <li><span class="social-mark"></span>gilded_critters</li>
      </ul>

      <div class="person">
        <h1 class="person-name">Daniel Workby</h1>
        <p class="person-title">Sales and Marketing</p>
        <div class="person-rule"></div>
      </div>

      <ul class="contact-list">
        <li>
          <svg class="contact-icon" viewBox="0 0 16 16" aria-hidden="true"><path fill="#ff9a0a" d="M3.6 1.5l2.3 2.6-1.3 1.9c.9 2 2.4 3.5 4.4 4.4l1.9-1.3 2.6 2.3-1.4 2.3C6.6 14.1 1.9 9.4 1.3 2.9z"/></svg>
          530-471-6328
        </li>
        <li>
          <svg class="contact-icon" viewBox="0 0 16 16" aria-hidden="true"><rect x="1" y="3" width="14" height="10" rx="1.5" fill="#ff9a0a"/><path d="M1.5 4l6.5 5 6.5-5" fill="none" stroke="#262627" stroke-width="1.4"/></svg>
          info@gildedcritters.example
        </li>
        <li>
          <svg class="contact-icon" viewBox="0 0 16 16" aria-hidden="true"><circle cx="8" cy="8" r="7" fill="#ff9a0a"/><path d="M1 8h14M8 1c-3 3.5-3 10.5 0 14M8 1c3 3.5 3 10.5 0 14" fill="none" stroke="#262627" stroke-width="1.1"/></svg>
          www.gildedcritters.example
        </li>
      </ul>
    </div>
  </section>

</body>
</html>
```